Beer Can Label design - HAZY NEIPA

Hazy NEIPA. (Acronym for New England India Pale Ale)
Full sleeve (473ml)
5.00" x 8.125" Inches
Write up on can reverse.
Opaque haze in appearance derived from specific oats, wheat, and water chemistry. This brew bolsters a dense and creamy head, leaving behind a soft and silky mouth-feel. Expect an intense tropical fruit centric aroma and flavour. Our timely hop additions contributes to less bitterness than typical IPA’s.
Logo is to be on front, towards bottom. Title near top.
Looking for something that stands out. Bold.
Target Market(s)
Craft beer enthusiasts
Industry/Entity Type
Beer & Brewing
Requirements
Must have
- Eye catching.

```html
<!DOCTYPE html>
<html lang="en">
<head>
<meta charset="UTF-8">
<title>Hazy NEIPA – Can Label</title>
<link href="https://fonts.googleapis.com/css2?family=Rye&family=Oswald:wght@300;400&display=swap" rel="stylesheet">
<style>
  :root {
    --label-green: #5a8a23;
    --sky-orange: #d48a32;
    --cream: #f4f1e6;
    --shadow-orange: #e0893a;
    --page: #ffffff;
  }
  * { margin: 0; padding: 0; box-sizing: border-box; }
  html, body {
    width: 1200px; height: 1000px; overflow: hidden;
    background: var(--page);
  }
  .canvas {
    position: relative; width: 1200px; height: 1000px;
    background: var(--page);
  }
  .can-label {
    position: absolute; left: 366px; top: 0;
    width: 467px; height: 1000px;
    background: var(--label-green);
    color: var(--cream);
    text-align: center;
    overflow: hidden;
  }
  .skyline {
    position: absolute; left: 0; top: 0; width: 100%; height: 180px;
    background: linear-gradient(to bottom, var(--sky-orange) 0%, var(--sky-orange) 62%, var(--label-green) 100%);
  }
  .title {
    position: absolute; left: 0; right: 0;
    font-family: "Rye", serif;
    color: var(--cream);
    text-shadow: 3px 3px 0 var(--shadow-orange);
    line-height: 1;
  }
  .title--main { top: 212px; font-size: 66px; letter-spacing: 1px; }
  .title--sub  { top: 386px; font-size: 66px; letter-spacing: 1px; }
  .title .hop-cone {
    display: inline-block; width: 36px; height: 56px;
    margin: 0 2px; vertical-align: -4px;
    background: var(--cream);
    border-radius: 50% 50% 50% 50% / 40% 40% 60% 60%;
    box-shadow: 3px 3px 0 var(--shadow-orange);
  }
  .for-the {
    position: absolute; left: 0; right: 0; top: 328px;
    display: flex; align-items: center; justify-content: center; gap: 14px;
    font-family: "Rye", serif; font-size: 36px;
    text-shadow: 2px 2px 0 var(--shadow-orange);
  }
  .for-the .rule { width: 110px; height: 3px; background: var(--cream); }
  .description {
    position: absolute; left: 48px; right: 48px; top: 506px;
    font-family: "Oswald", sans-serif; font-weight: 300;
    font-size: 14.5px; line-height: 1.42;
  }
  .brand-badge {
    position: absolute; left: 88px; top: 635px;
    width: 290px; height: 290px;
  }
  .brand-name {
    position: absolute; left: 0; right: 0; top: 118px;
    font-family: "Rye", serif; font-size: 40px; line-height: 1.05;
    color: var(--cream);
  }
  .brand-name small { display: block; font-size: 20px; letter-spacing: 6px; margin-top: 8px; }
  .volume {
    position: absolute; left: 0; right: 0; top: 955px;
    font-family: "Oswald", sans-serif; font-weight: 400; font-size: 22px;
  }
</style>
</head>
<body>
<div class="canvas">
  <section class="can-label">
    <div class="skyline" role="img" aria-label="Silhouette of an industrial city skyline with smokestacks against an orange sky"></div>

    <h1 class="title title--main">HAZY NEIPA</h1>
    <div class="for-the"><span class="rule"></span>FOR THE<span class="rule"></span></div>
    <h2 class="title title--sub">H<span class="hop-cone" role="img" aria-label="Hop cone illustration standing in for the letter O"></span>P HEADS</h2>

    <p class="description">Opaque haze in appearance derived from specific oats, wheat, and water chemistry. This brew bolsters a dense and creamy head, leaving behind a soft and silky mouth-feel. Expect an intense tropical fruit centric aroma and flavour. Our timely hop additions contributes to less bitterness than typical IPA’s.</p>

    <div class="brand-badge">
      <svg width="290" height="290" viewBox="0 0 290 290" aria-hidden="true">
        <circle cx="145" cy="145" r="142" fill="none" stroke="#f4f1e6" stroke-width="3"/>
      </svg>
      <div class="brand-name">HARBOR STACK<small>BREW HOUSE</small></div>
    </div>

    <div class="volume">473 ml</div>
  </section>
</div>
</body>
</html>
```